Silver Creek Plumbing Business card & letter head design

We need a new business card and letter head for our plumbing company called silver creek plumbing. attached is the companys logo. We provide domestic and commercial plumbing services in regional western Australia. We are after Something simple yet nice to look at and something that fits within the trade industry.

Target Market(s)

trade/building industry

Contact Information for Business Card

Darl Hensby
Manager
0461 238 574
enquiries@scplumbwork.net.au
ABN: 47 381 905 462
PCL: 5187

Domestic & Commercial Plumbing
Tip Truck & Excavator hire

Colors

Designer to choose colors to be used in the design.

```html
<!DOCTYPE html>
<html lang="en">
<head>
<meta charset="utf-8">
<title>Silver Creek Plumbing – Letterhead</title>
<link rel="stylesheet" href="https://fonts.googleapis.com/css2?family=Open+Sans:wght@400;700&display=swap">
<style>
  :root {
    --brand-blue: #1a73b8;
    --brand-navy: #1f3f8f;
    --rule-grey: #4a4a4a;
    --text-grey: #4d4d4d;
    --paper: #ffffff;
    --backdrop: #dfe7e8;
  }
  * { box-sizing: border-box; margin: 0; padding: 0; }
  html, body {
    width: 1200px; height: 1000px; overflow: hidden;
    background: var(--backdrop);
    font-family: "Open Sans", Arial, sans-serif;
    color: var(--text-grey);
  }
  .letterhead {
    position: absolute; left: 282px; top: 50px;
    width: 636px; height: 900px;
    background: var(--paper);
    box-shadow: 0 4px 18px rgba(0,0,0,.12);
    overflow: hidden;
  }
  .corner-tab {
    position: absolute; left: 36px; top: 0;
    width: 64px; height: 22px; background: var(--brand-blue);
  }
  .brand {
    position: absolute; left: 60px; top: 46px;
    display: flex; align-items: center; gap: 10px;
  }
  .brand-mark { width: 18px; height: 18px; background: var(--brand-blue); }
  .brand-name {
    font-weight: 700; font-size: 21px; color: var(--brand-navy);
    letter-spacing: .2px;
  }
  .header-swoosh { position: absolute; left: 0; top: 78px; width: 636px; height: 140px; }
  .contact {
    position: absolute; right: 24px; top: 84px;
    display: flex; gap: 8px; align-items: flex-start;
  }
  .contact-lines { text-align: right; font-size: 8.5px; line-height: 12.5px; }
  .contact-icons { display: flex; flex-direction: column; gap: 3px; }
  .contact-icon {
    width: 14px; height: 14px; background: var(--brand-blue);
    display: flex; align-items: center; justify-content: center;
  }
  .contact-icon svg { width: 9px; height: 9px; }
  .letter {
    position: absolute; left: 60px; top: 236px; width: 516px;
    font-size: 10.5px; line-height: 15px;
  }
  .letter-date { text-align: right; margin-bottom: 18px; }
  .recipient { margin-bottom: 14px; }
  .letter p { margin-bottom: 12px; }
  .signature-block { margin-top: 14px; }
  .footer-rule {
    position: absolute; left: 0; right: 0; bottom: 96px;
    height: 5px; background: var(--rule-grey);
  }
  .footer-band {
    position: absolute; left: 0; right: 0; bottom: 0;
    height: 80px; background: var(--brand-blue);
  }
</style>
</head>
<body>
  <main class="letterhead">
    <div class="corner-tab"></div>

    <div class="brand">
      <span class="brand-mark"></span>
      <span class="brand-name">Silver Creek Plumbing</span>
    </div>

    <svg class="header-swoosh" viewBox="0 0 636 140" preserveAspectRatio="none" aria-hidden="true">
      <defs>
        <linearGradient id="swoosh-fade" x1="0" x2="1">
          <stop offset="0" stop-color="#1f3f8f"/>
          <stop offset=".6" stop-color="#1a73b8"/>
          <stop offset="1" stop-color="#c9d3e6"/>
        </linearGradient>
      </defs>
      <path d="M40 4 C 260 10, 420 70, 636 130" fill="none" stroke="url(#swoosh-fade)" stroke-width="2"/>
    </svg>

    <div class="contact">
      <div class="contact-lines">
        <div>0461 238 574</div>
        <div>enquiries@scplumbwork.net.au</div>
        <div>www.scplumbwork.net.au</div>
        <div>ABN: 47 381 905 462</div>
        <div>PCL: 5187</div>
      </div>
      <div class="contact-icons">
        <span class="contact-icon">
          <svg viewBox="0 0 10 10"><path d="M2 1l2 2-1 1.5c.8 1.4 1.5 2.1 2.5 2.5L7 6l2 2-1.5 1.5C4.5 9 1 5.5.5 2.5z" fill="#fff"/></svg>
        </span>
        <span class="contact-icon">
          <svg viewBox="0 0 10 10"><rect x="1" y="2.5" width="8" height="5.5" fill="none" stroke="#fff" stroke-width="1"/><path d="M1 2.5l4 3 4-3" fill="none" stroke="#fff" stroke-width="1"/></svg>
        </span>
        <span class="contact-icon">
          <svg viewBox="0 0 10 10"><circle cx="5" cy="5" r="3.8" fill="none" stroke="#fff" stroke-width="1"/><path d="M1.2 5h7.6M5 1.2c-2 2.5-2 5.1 0 7.6M5 1.2c2 2.5 2 5.1 0 7.6" fill="none" stroke="#fff" stroke-width=".8"/></svg>
        </span>
      </div>
    </div>

    <article class="letter">
      <div class="letter-date">December 03, 2019</div>
      <div class="recipient">
        Mr. Owen Marsh<br>
        Marsh Holdings<br>
        1234 Harbour View Lane<br>
        Bay Town, WA 6000
      </div>
      <p>Dear Mr. Marsh:</p>
      <p>The first paragraph of a typical business letter is used to state the main point of the letter. Begin with a friendly opening; then quickly transition into the purpose of your letter. Use a couple of sentences to explain the purpose, but do not go in to detail until the next paragraph.</p>
      <p>Beginning with the second paragraph, state the supporting details to justify your purpose. These may take the form of background information, statistics or first-hand accounts. A few short paragraphs within the body of the letter should be enough to support your reasoning.</p>
      <p>Finally, in the closing paragraph, briefly restate your purpose and why it is important. If the purpose of your letter is related to your employment, consider ending your letter with your contact information and title if it not included on letterhead. However, if the purpose is informational, think about closing with gratitude for the reader's time.</p>
      <div class="signature-block">
        <p>Sincerely,</p>
        <p>&lt;SIGNATURE GOES HERE&gt;</p>
        <div>Nora Pell<br>President</div>
      </div>
    </article>

    <div class="footer-rule"></div>
    <div class="footer-band"></div>
  </main>
</body>
</html>
```